BUSINESS CARD-POST CARD-LETTERHEAD-ENVELOPES
LOOKING FOR AN AWSOME BUSINESS CARD,LETTERHEAD,POSTCARD
Professional
Tom Beluno
President
5172 Wrenfield
Larkmoor Heights, MI 48190
tombeluno@mailverta.com
www.boldwavez.com
we are a digital printing company who specializes in mainly business cards,post cards, and web sites, we do also do a little bit of posters, flyers, and brochures. Our business name is BOLDWAVE MEDIA, reason being is that we want people to know that we do not use templets everything is custom built, so we are looking for something that is very eye catching and a design that will blow people away. we are also looking for a postcard for mailing advertisements or promotions. I will provide all my logos use whichever ones you would like and let your imagination go. I will also need to be able to edit the cards and info for different people and incase we change our address.
maybe a listing of all the products we offer or any thing you think would look great, ill leave it up to you.

```html
<!DOCTYPE html>
<html lang="en">
<head>
<meta charset="utf-8">
<title>Boldwave Media – Business Cards</title>
<link href="https://fonts.googleapis.com/css2?family=Arimo:wght@400;700&display=swap" rel="stylesheet">
<style>
  :root {
    --bg: #e9e6e1;
    --card: #ffffff;
    --band-dark: #0c3346;
    --band-mid: #1b6a86;
    --band-light: #2f8fae;
    --green: #6e9a1f;
    --green-light: #a5c94a;
    --brand: #1d5e7a;
    --ink: #4a4f54;
    --rule: #c9ced2;
  }
  * { box-sizing: border-box; margin: 0; padding: 0; }
  html, body { width: 1200px; height: 852px; overflow: hidden; }
  body {
    background: var(--bg);
    font-family: "Arimo", Arial, sans-serif;
    position: relative;
  }
  .card {
    position: absolute;
    width: 560px;
    height: 320px;
    background: var(--card);
    border-radius: 22px;
    overflow: hidden;
    box-shadow: 0 10px 28px rgba(0,0,0,.22);
  }
  .card--stacked { left: 70px; top: 70px; }
  .card--centered { left: 570px; top: 462px; }
  .card__band { position: absolute; left: 0; top: 0; width: 560px; height: 130px; }
  .card__holder {
    position: absolute; right: 34px; top: 22px;
    text-align: right; color: #fff;
  }
  .card__name { font-weight: 700; font-size: 17px; letter-spacing: .2px; }
  .card__title { font-size: 12px; margin-top: 5px; }
  .brand {
    position: absolute;
    display: flex; align-items: center; gap: 8px;
  }
  .brand__mark { width: 26px; height: 26px; background: var(--green); flex: none; }
  .brand__name {
    font-weight: 700; font-size: 20px; color: var(--brand);
    letter-spacing: .4px; white-space: nowrap;
  }
  .divider { position: absolute; width: 1px; background: var(--rule); }
  .address { position: absolute; font-size: 13px; color: var(--ink); line-height: 1.45; white-space: nowrap; }
  .contacts { position: absolute; list-style: none; font-size: 13px; color: var(--ink); }
  .contacts li { display: flex; align-items: center; gap: 7px; height: 21px; white-space: nowrap; }
  .contacts svg { width: 13px; height: 13px; flex: none; }

  .card--stacked .brand { left: 28px; top: 192px; }
  .card--stacked .divider { left: 292px; top: 150px; height: 135px; }
  .card--stacked .address { left: 312px; top: 155px; }
  .card--stacked .contacts { left: 312px; top: 210px; }

  .card--centered .brand { left: 144px; top: 154px; }
  .card--centered .divider { left: 300px; top: 205px; height: 80px; }
  .card--centered .address { right: 276px; top: 222px; text-align: right; }
  .card--centered .contacts { left: 318px; top: 210px; }
</style>
</head>
<body>

<svg width="0" height="0" style="position:absolute" aria-hidden="true">
  <defs>
    <linearGradient id="bandFill" x1="0" y1="0" x2="1" y2="0.4">
      <stop offset="0" stop-color="#0c3346"/>
      <stop offset=".55" stop-color="#1b6a86"/>
      <stop offset="1" stop-color="#2f8fae"/>
    </linearGradient>
    <linearGradient id="swoosh" x1="0" y1="0" x2="1" y2="0">
      <stop offset="0" stop-color="#6e9a1f"/>
      <stop offset="1" stop-color="#a5c94a"/>
    </linearGradient>
    <symbol id="ico-phone" viewBox="0 0 16 16">
      <rect x="4" y="1" width="8" height="14" rx="2" fill="#1b6a86"/>
      <rect x="5.5" y="3" width="5" height="8" fill="#fff"/>
      <circle cx="8" cy="13" r=".9" fill="#fff"/>
    </symbol>
    <symbol id="ico-mail" viewBox="0 0 16 16">
      <circle cx="8" cy="8" r="7.5" fill="#1b6a86"/>
      <rect x="3.5" y="5" width="9" height="6" fill="#fff"/>
      <path d="M3.5 5 L8 8.5 L12.5 5" stroke="#1b6a86" fill="none" stroke-width="1"/>
    </symbol>
    <symbol id="ico-web" viewBox="0 0 16 16">
      <circle cx="8" cy="8" r="7.5" fill="#2f8fae"/>
      <ellipse cx="8" cy="8" rx="3" ry="6" fill="none" stroke="#fff" stroke-width="1"/>
      <line x1="2" y1="8" x2="14" y2="8" stroke="#fff" stroke-width="1"/>
    </symbol>
  </defs>
</svg>

<article class="card card--stacked">
  <svg class="card__band" viewBox="0 0 560 130" aria-hidden="true">
    <path d="M0 0 H560 V96 C420 50 260 52 0 84 Z" fill="url(#bandFill)"/>
    <path d="M0 92 C260 60 420 58 560 104 V110 C420 68 260 70 0 100 Z" fill="url(#swoosh)"/>
  </svg>
  <div class="card__holder">
    <div class="card__name">Tom Beluno</div>
    <div class="card__title">President</div>
  </div>
  <div class="brand">
    <span class="brand__mark"></span>
    <span class="brand__name">BOLDWAVE MEDIA</span>
  </div>
  <div class="divider"></div>
  <p class="address">5172 Wrenfield<br>Larkmoor Heights, MI 48190</p>
  <ul class="contacts">
    <li><svg><use href="#ico-phone"/></svg>313.555.0142</li>
    <li><svg><use href="#ico-mail"/></svg>tombeluno@mailverta.com</li>
    <li><svg><use href="#ico-web"/></svg>www.boldwavez.com</li>
  </ul>
</article>

<article class="card card--centered">
  <svg class="card__band" viewBox="0 0 560 130" aria-hidden="true">
    <path d="M0 0 H560 V96 C420 50 260 52 0 84 Z" fill="url(#bandFill)"/>
    <path d="M0 92 C260 60 420 58 560 104 V110 C420 68 260 70 0 100 Z" fill="url(#swoosh)"/>
  </svg>
  <div class="card__holder">
    <div class="card__name">Tom Beluno</div>
    <div class="card__title">President</div>
  </div>
  <div class="brand">
    <span class="brand__mark"></span>
    <span class="brand__name">BOLDWAVE MEDIA</span>
  </div>
  <div class="divider"></div>
  <p class="address">5172 Wrenfield<br>Larkmoor Heights, MI 48190</p>
  <ul class="contacts">
    <li><svg><use href="#ico-phone"/></svg>313.555.0142</li>
    <li><svg><use href="#ico-mail"/></svg>tombeluno@mailverta.com</li>
    <li><svg><use href="#ico-web"/></svg>www.boldwavez.com</li>
  </ul>
</article>

</body>
</html>
```